Business Card Design and a letter head logo

50/50 share milker dairy farmer of 400 cows with a silage and haymaking sideline business
15 years farming currently looking for new opportunities within the dairy farming sector. trying to put together a portfolio to get another 50/50 share milking job aswell

Industry/Entity Type

Farming

Contact Information for Business Card

Birch Farming LTD
Corwin & Felicity Hartley
382 Kelvale Ridge Highway
RD1 Tawhiro 0184
Whangarei
hartley.corwin@lumenmail.co.nz
0273948261
(09) 4715293

```html
<!DOCTYPE html>
<html lang="en">
<head>
<meta charset="utf-8">
<title>Birch Farming LTD – Letterhead and Business Card</title>
<link rel="stylesheet" href="https://fonts.googleapis.com/css2?family=Libre+Baskerville:wght@400;700&family=PT+Sans:wght@400;700&display=swap">
<style>
  :root {
    --backdrop: #ebe8e3;
    --paper: #ffffff;
    --brand-green: #2f9c3c;
    --leaf-light: #dcefc9;
    --leaf-ring: #6cc04a;
    --sky-deep: #58aee3;
    --sky-light: #cfe8f8;
    --grass: #4caf3d;
    --grass-light: #a9d86b;
    --ink: #1e1e1e;
    --ink-soft: #3c3c3c;
  }
  * { box-sizing: border-box; margin: 0; padding: 0; }
  html, body { width: 1200px; height: 1000px; overflow: hidden; }
  body { background: var(--backdrop); position: relative; font-family: "PT Sans", sans-serif; color: var(--ink); }

  .sheet { position: absolute; background: var(--paper); box-shadow: 0 2px 8px rgba(0,0,0,.18); overflow: hidden; }
  .letterhead { left: 72px; top: 88px; width: 631px; height: 845px; }
  .business-card { left: 830px; top: 322px; width: 275px; height: 459px; }

  .brand { position: absolute; left: 50%; transform: translateX(-50%); text-align: center; }
  .brand-circle { display: block; margin: 0 auto; border-radius: 50%; background: var(--leaf-light); border: 4px solid var(--leaf-ring); }
  .brand-name { display: block; font-family: "Libre Baskerville", serif; font-weight: 400; color: var(--brand-green); text-transform: uppercase; white-space: nowrap; }

  .letterhead .brand { top: 15px; }
  .letterhead .brand-circle { width: 150px; height: 150px; }
  .letterhead .brand-name { font-size: 21px; margin-top: 22px; }

  .business-card .brand { top: 26px; }
  .business-card .brand-circle { width: 128px; height: 128px; }
  .business-card .brand-name { font-size: 17px; margin-top: 22px; }

  .icon { width: 9px; height: 9px; vertical-align: -1px; margin-right: 3px; fill: var(--brand-green); }

  .letterhead-contact { position: absolute; left: 0; right: 0; top: 665px; text-align: center; font-size: 11.5px; color: var(--ink-soft); line-height: 16px; margin-left: -34px; }
  .letterhead-contact .gap { display: inline-block; width: 12px; }

  .card-details { position: absolute; left: 0; right: 0; top: 224px; text-align: center; font-size: 10.5px; line-height: 15px; }
  .card-holders { font-family: "Libre Baskerville", serif; font-size: 13px; margin-bottom: 12px; }
  .card-visit { margin-top: 18px; }
  .card-visit strong { font-weight: 700; display: block; }

  .meadow-band { position: absolute; left: 0; bottom: 0; display: block; }
</style>
</head>
<body>

<section class="sheet letterhead">
  <div class="brand">
    <span class="brand-circle"></span>
    <span class="brand-name">Birch Farming LTD</span>
  </div>

  <div class="letterhead-contact">
    <p>
      <svg class="icon" viewBox="0 0 10 10"><path d="M2 0.5l2 2-1 1.2c.6 1.3 1.6 2.3 2.8 2.8l1.2-1 2 2-1.3 1.8C4 9 1 6 .3 1.8z"/></svg>0273948261 / (09) 4715293<span class="gap"></span>
      <svg class="icon" viewBox="0 0 10 10"><path d="M0 2h10v6H0z"/><path d="M0 2l5 3.5L10 2" fill="none" stroke="#fff" stroke-width="1"/></svg>hartley.corwin@lumenmail.co.nz
    </p>
    <p>382 Kelvale Ridge Highway RD1 Tawhiro 0184</p>
  </div>

  <svg class="meadow-band" width="631" height="160" viewBox="0 0 631 160">
    <defs>
      <linearGradient id="lh-sky" x1="0" y1="0" x2="0" y2="1">
        <stop offset="0" stop-color="var(--sky-deep)"/>
        <stop offset="1" stop-color="var(--sky-light)"/>
      </linearGradient>
      <linearGradient id="lh-grass" x1="0" y1="0" x2="1" y2="0">
        <stop offset="0" stop-color="var(--grass)"/>
        <stop offset="1" stop-color="var(--grass-light)"/>
      </linearGradient>
    </defs>
    <path d="M0 22 C160 4 330 28 470 16 C540 10 590 4 631 0 V110 C480 140 300 150 0 118 Z" fill="url(#lh-sky)"/>
    <path d="M0 30 C170 14 340 36 480 24 C560 18 600 12 631 10" fill="none" stroke="#fff" stroke-width="3"/>
    <rect role="img" aria-label="Illustration of a brown and white cow and a black and white cow grazing on green pasture" x="0" y="50" width="440" height="90" fill="url(#lh-sky)" opacity="0.6"/>
    <path d="M0 130 C200 150 420 142 631 112 V116 C420 150 200 160 0 146 Z" fill="url(#lh-grass)"/>
  </svg>
</section>

<section class="sheet business-card">
  <div class="brand">
    <span class="brand-circle"></span>
    <span class="brand-name">Birch Farming LTD</span>
  </div>

  <div class="card-details">
    <p class="card-holders">Corwin &amp; Felicity Hartley</p>
    <p><svg class="icon" viewBox="0 0 10 10"><path d="M2 0.5l2 2-1 1.2c.6 1.3 1.6 2.3 2.8 2.8l1.2-1 2 2-1.3 1.8C4 9 1 6 .3 1.8z"/></svg>0273948261</p>
    <p><svg class="icon" viewBox="0 0 10 10"><path d="M2 0.5l2 2-1 1.2c.6 1.3 1.6 2.3 2.8 2.8l1.2-1 2 2-1.3 1.8C4 9 1 6 .3 1.8z"/></svg>(09) 4715293</p>
    <p><svg class="icon" viewBox="0 0 10 10"><path d="M0 2h10v6H0z"/><path d="M0 2l5 3.5L10 2" fill="none" stroke="#fff" stroke-width="1"/></svg>hartley.corwin@lumenmail.co.nz</p>
    <p class="card-visit"><strong>Visit us at:</strong>382 Kelvale Ridge Highway RD1 Tawhiro<br>0184 Whangarei</p>
  </div>

  <svg class="meadow-band" width="275" height="100" viewBox="0 0 275 100">
    <defs>
      <linearGradient id="bc-sky" x1="0" y1="0" x2="0" y2="1">
        <stop offset="0" stop-color="var(--sky-deep)"/>
        <stop offset="1" stop-color="var(--sky-light)"/>
      </linearGradient>
      <linearGradient id="bc-grass" x1="0" y1="0" x2="1" y2="0">
        <stop offset="0" stop-color="var(--grass)"/>
        <stop offset="1" stop-color="var(--grass-light)"/>
      </linearGradient>
    </defs>
    <path d="M0 14 C80 2 170 16 275 4 V66 C190 84 100 88 0 76 Z" fill="url(#bc-sky)"/>
    <path d="M0 20 C80 8 170 22 275 10" fill="none" stroke="#fff" stroke-width="2"/>
    <rect role="img" aria-label="Illustration of a brown and white cow and a black and white cow on green pasture" x="0" y="28" width="195" height="56" fill="url(#bc-sky)" opacity="0.6"/>
    <path d="M0 80 C90 92 180 88 275 70 V74 C180 94 90 98 0 90 Z" fill="url(#bc-grass)"/>
  </svg>
</section>

</body>
</html>
```